New Podcast, Ridgewater Wellness Bureaus

We need a cover design for a new podcast that we are producing.

Title: Ridgewater Wellness Bureaus

This is a business podcast for Native American tribal organizations, representing indigenous peoples of the United States.

Pull colors from the logo.
Do not add photos of people into the design.

Public Health, Statistics, Epidemiology, Tribal Organizations, NonProfits

```html
<!DOCTYPE html>
<html lang="en">
<head>
<meta charset="utf-8">
<title>Ridgewater Wellness Bureaus — Podcast Cover</title>
<link href="https://fonts.googleapis.com/css2?family=Montserrat:wght@800&display=swap" rel="stylesheet">
<style>
  :root {
    --backdrop: #f7dc8a;
    --teal-light: #2a9aa6;
    --teal-mid: #1a8391;
    --teal-deep: #0d5f6b;
    --ring-bright: #27a9b7;
    --mic-cream: #f3e7cb;
    --bar-white: #ffffff;
    --band-orange: #cb6b22;
    --plate-white: #ffffff;
    --name-ink: #c8651f;
  }
  * { margin: 0; padding: 0; box-sizing: border-box; }
  html, body {
    width: 1200px;
    height: 890px;
    overflow: hidden;
    background: var(--backdrop);
  }
  .stage {
    position: relative;
    width: 1200px;
    height: 890px;
  }
  .podcast-cover {
    position: absolute;
    left: 270px;
    top: 115px;
    width: 660px;
    height: 660px;
    display: block;
  }
  .brand-name {
    font-family: "Montserrat", "Helvetica Neue", Arial, sans-serif;
    font-weight: 800;
    fill: var(--name-ink);
  }
</style>
</head>
<body>
<main class="stage">
  <svg class="podcast-cover" viewBox="0 0 660 660" xmlns="http://www.w3.org/2000/svg" aria-label="Ridgewater Wellness Bureaus podcast cover">
    <defs>
      <radialGradient id="teal-glow" cx="50%" cy="35%" r="75%">
        <stop offset="0" stop-color="var(--teal-light)"/>
        <stop offset="0.6" stop-color="var(--teal-mid)"/>
        <stop offset="1" stop-color="var(--teal-deep)"/>
      </radialGradient>
    </defs>

    <!-- teal field -->
    <rect class="cover-field" x="0" y="0" width="660" height="540" fill="url(#teal-glow)"
          role="img" aria-label="Teal sunburst background with flowing sound wave lines"/>

    <!-- microphone badge -->
    <g class="mic-badge">
      <circle cx="330" cy="252" r="122" fill="var(--teal-deep)"/>
      <circle cx="330" cy="252" r="98" fill="var(--ring-bright)"/>
      <circle cx="330" cy="252" r="82" fill="var(--teal-deep)"/>
      <g class="mic-icon" fill="none" stroke="var(--mic-cream)" stroke-linecap="round">
        <rect x="305" y="195" width="50" height="100" rx="25" fill="var(--mic-cream)" stroke="none"/>
        <g stroke="var(--teal-deep)" stroke-width="4">
          <line x1="312" y1="220" x2="348" y2="220"/>
          <line x1="312" y1="234" x2="348" y2="234"/>
          <line x1="312" y1="248" x2="348" y2="248"/>
        </g>
        <path d="M287 268 Q287 318 330 318 Q373 318 373 268" stroke-width="9"/>
        <line x1="330" y1="318" x2="330" y2="345" stroke-width="9"/>
      </g>
    </g>

    <!-- sound level bars -->
    <g class="sound-bars" fill="var(--bar-white)">
      <rect x="166" y="442" width="8" height="26" rx="2"/>
      <rect x="183" y="432" width="8" height="46" rx="2"/>
      <rect x="200" y="422" width="8" height="66" rx="2"/>
      <rect x="217" y="436" width="8" height="38" rx="2"/>
      <rect x="234" y="414" width="8" height="82" rx="2"/>
      <rect x="251" y="428" width="8" height="54" rx="2"/>
      <rect x="268" y="440" width="8" height="30" rx="2"/>
      <rect x="285" y="420" width="8" height="70" rx="2"/>
      <rect x="302" y="432" width="8" height="46" rx="2"/>
      <rect x="319" y="410" width="8" height="90" rx="2"/>
      <rect x="336" y="426" width="8" height="58" rx="2"/>
      <rect x="353" y="438" width="8" height="34" rx="2"/>
      <rect x="370" y="418" width="8" height="74" rx="2"/>
      <rect x="387" y="430" width="8" height="50" rx="2"/>
      <rect x="404" y="440" width="8" height="30" rx="2"/>
      <rect x="421" y="416" width="8" height="78" rx="2"/>
      <rect x="438" y="428" width="8" height="54" rx="2"/>
      <rect x="455" y="436" width="8" height="38" rx="2"/>
      <rect x="472" y="424" width="8" height="62" rx="2"/>
      <rect x="489" y="442" width="8" height="26" rx="2"/>
    </g>

    <!-- footer band -->
    <rect class="divider-line" x="0" y="540" width="660" height="7" fill="var(--plate-white)"/>
    <rect class="footer-band" x="0" y="547" width="660" height="113" fill="var(--band-orange)"/>
    <polygon class="name-plate" points="192,547 598,547 566,660 224,660" fill="var(--plate-white)"/>

    <!-- organisation name -->
    <g class="brand-lockup">
      <circle cx="262" cy="603" r="30" fill="var(--band-orange)"/>
      <text class="brand-name" x="306" y="596" font-size="22">RIDGEWATER</text>
      <text class="brand-name" x="306" y="623" font-size="16">WELLNESS BUREAUS</text>
    </g>
  </svg>
</main>
</body>
</html>
```